Re-brand our business and design!

We need a simple informational website (editable for in the future use)
We need our logo(we have included logo), name, who we are, and what we do displayed.

This is our current site (which is not acceptable, and only a template site): all our information is on this site, please use it forreferanceofinformation.
Www.brightlanefixers.com

Target Market(s)

Real estate brokers, and realtors,homeowners, and anyone looking for home repairs.

Industry/Entity Type

Business

Number of Pages Required

4 page

Font styles to use
Sans Serif

Requirements
Must have
• Our name, contact info, services, and our logo (which we will Email upon request)
• MUST have originality to the site.
• custom "contact us form" or request an estimate form.
Nice to have
• page for real customer testimonies.
• page for our previous work where we can upload pics of completed jobs.
Should not have
• any infringements on any copyrights or plagiarism at all.

```html
<!DOCTYPE html>
<html lang="en">
<head>
<meta charset="utf-8">
<title>Bright Lane Fixers And Maintenance</title>
<link href="https://fonts.googleapis.com/css2?family=Open+Sans:wght@400;600;700&display=swap" rel="stylesheet">
<style>
:root{
  --red:#e0191c;
  --red-dark:#b81215;
  --black:#0b0b0b;
  --ink:#1a1a1a;
  --body:#333;
  --grey:#8a8a8a;
  --light:#eef0f2;
  --white:#fff;
  --footer:#1c1b1a;
}
*{box-sizing:border-box;margin:0;padding:0}
html,body{width:1200px;height:3509px;overflow:hidden}
body{position:relative;font-family:'Open Sans',Arial,sans-serif;color:var(--body);background:var(--white)}
.abs{position:absolute}
.accent{color:var(--red)}

/* header */
.topbar{left:456px;top:0;width:744px;height:40px;background:var(--red);color:var(--white);font-size:16px;display:flex;align-items:center}
.topbar .item{display:flex;align-items:center;gap:10px;margin-left:34px}
.topbar .estimate{position:absolute;left:468px;top:0;width:194px;height:40px;background:#bdbdbd;color:#333;display:flex;align-items:center;gap:10px;padding-left:14px;font-size:15px}
.topbar .tail{position:absolute;left:662px;top:0;width:82px;height:40px;background:var(--black)}
.navbar{left:456px;top:40px;width:744px;height:93px;background:var(--black)}
.nav a{position:absolute;top:74px;color:var(--white);text-decoration:none;font-size:16px;font-weight:600}
.nav a.current{color:var(--red)}
.logo-panel{left:0;top:0;width:520px;height:133px}
.brand{left:78px;top:28px;font-size:27px;font-weight:700;color:var(--ink);line-height:1.15}
.brand-mark{left:40px;top:36px;width:26px;height:26px;background:var(--red)}

/* hero */
.hero{left:0;top:133px;width:1200px;height:550px;background:linear-gradient(100deg,#6e2a25 0%,#9a3b31 35%,#b9574a 60%,#8c3329 100%)}
.hero h1{position:absolute;left:84px;top:242px;color:var(--white);font-size:46px;font-weight:600;line-height:1.25}
.hero .dashes{position:absolute;left:84px;top:384px;display:flex;gap:8px}
.hero .dashes span{display:block;height:4px;width:16px;background:var(--white)}
.hero .dashes span:first-child{width:22px;background:var(--red)}

/* titles */
.title{width:1200px;text-align:center;font-size:35px;font-weight:700;color:var(--ink)}
.title.light{color:var(--white)}
.title.small{font-size:33px}

.btn{display:flex;align-items:center;justify-content:center;background:var(--red);color:var(--white);font-size:15px;font-weight:600}

/* welcome */
.welcome-text{left:94px;top:810px;width:1016px;text-align:center;font-size:14.5px;line-height:22px;color:#444}

/* services */
.services{left:0;top:1006px;width:1200px;height:470px;background:linear-gradient(180deg,#2d2d2d,#3b3b3b 50%,#262626)}
.card{position:absolute;top:114px;width:250px;height:293px}
.card .photo{height:195px}
.card .label{height:98px;background:var(--black);color:var(--white);font-size:25px;display:flex;align-items:center;justify-content:center}
.card.active .label{background:var(--red)}
.arrow{position:absolute;top:250px;width:26px;height:26px;background:#e6e6e6;display:flex;align-items:center;justify-content:center}

/* projects */
.projects{left:0;top:1609px;width:1200px;height:239px;display:flex}
.projects .tile{flex:1;position:relative}
.tile .overlay{position:absolute;inset:0;background:rgba(224,25,28,.85);color:var(--white);text-align:center;padding-top:48px}
.overlay h3{font-size:22px;font-weight:600}
.overlay p{font-size:13px;line-height:17px;margin-top:10px;padding:0 24px}
.overlay .icons{display:flex;justify-content:center;gap:10px;margin-top:20px}
.overlay .icons span{width:30px;height:30px;border:2px solid var(--white);display:flex;align-items:center;justify-content:center}

/* why */
.why{left:0;top:1981px;width:1200px;height:564px;background:linear-gradient(90deg,#e8eaec,#f3f4f6 60%,#e9ebed)}
.feature{position:absolute;left:84px;width:620px}
.feature .icon{position:absolute;left:0;top:0;width:76px;height:76px;border-radius:50%;background:#4a4a4a;border:5px solid #c9c9c9;display:flex;align-items:center;justify-content:center}
.feature h4{position:absolute;left:94px;top:2px;font-size:21px;font-weight:700;color:var(--ink)}
.feature p{position:absolute;left:94px;top:36px;width:520px;font-size:14.5px;line-height:22px;color:#444}
.rule{position:absolute;left:84px;width:640px;height:1px;background:#cfd2d5}
.workers{left:713px;top:2077px;width:487px;height:468px;background:linear-gradient(180deg,#d8dbe0,#b79a6c 55%,#7a6a52)}

/* testimonials */
.quote{left:206px;top:2680px;width:790px;text-align:center;font-size:14.5px;line-height:24px;color:#444}
.qmark{top:2678px;font-size:110px;line-height:1;color:#c9c9c9;font-family:Georgia,serif}
.avatar{position:absolute;border-radius:50%;background:radial-gradient(circle at 50% 40%,#d9c2ae,#8d7866)}
.dots{left:556px;top:2972px;display:flex;gap:6px}
.dots span{width:11px;height:11px;border-radius:50%;background:#cfcfcf}
.dots span.on{background:var(--red)}

/* footer */
.footer{left:0;top:3031px;width:1200px;height:478px;background:linear-gradient(180deg,#232221,#181716)}
.fnav a{position:absolute;top:3064px;color:#e8e8e8;text-decoration:none;font-size:17px}
.fnav .sep{position:absolute;top:3073px;width:7px;height:7px;background:#666}
.fline{left:0;top:3118px;width:1200px;height:1px;background:#444}
.contact{position:absolute;left:78px;width:360px;color:#ddd}
.contact .ring{position:absolute;left:0;top:0;width:46px;height:46px;border-radius:50%;border:2px solid #ddd;display:flex;align-items:center;justify-content:center}
.contact h5{position:absolute;left:84px;top:0;font-size:17px;font-weight:700;color:var(--white)}
.contact p{position:absolute;left:84px;top:30px;font-size:14px;line-height:21px}
.form-title{left:472px;top:3154px;font-size:17px;font-weight:700;color:var(--white)}
.field{position:absolute;left:482px;width:266px;height:38px;border:1px solid #555;background:rgba(0,0,0,.25);color:#ccc;font-size:13px;padding:10px 12px}
.message{left:772px;top:3205px;width:346px;height:182px;border:1px solid #555;background:rgba(0,0,0,.25);color:#ccc;font-size:13px;padding:10px 12px}
.submit{left:919px;top:3406px;width:199px;height:34px}
.bottom{left:0;top:3466px;width:1200px;height:43px;background:var(--black);color:#cfcfcf;font-size:13px}
.social{position:absolute;top:12px;width:22px;height:22px;background:#3b5998}
</style>
</head>
<body>

<!-- header -->
<div class="abs logo-panel"></div>
<div class="abs brand-mark"></div>
<div class="abs brand">Bright Lane Fixers<br>And Maintenance</div>
<svg class="abs" style="left:400px;top:0" width="160" height="133"><polygon points="0,0 56,0 160,133 120,133" fill="#ffffff"/></svg>

<div class="abs topbar">
  <div class="item">
    <svg width="14" height="14" viewBox="0 0 24 24"><path d="M6.6 10.8a15 15 0 0 0 6.6 6.6l2.2-2.2c.3-.3.7-.4 1-.2 1.1.4 2.3.6 3.6.6.6 0 1 .4 1 1V20c0 .6-.4 1-1 1C10.6 21 3 13.4 3 4c0-.6.4-1 1-1h3.5c.6 0 1 .4 1 1 0 1.3.2 2.5.6 3.6.1.3 0 .7-.2 1z" fill="#000"/></svg>
    <span>555-214-0937</span>
  </div>
  <div class="item">
    <svg width="16" height="12" viewBox="0 0 16 12"><rect width="16" height="12" rx="2" fill="#000"/><path d="M1 1l7 6 7-6" stroke="#e0191c" stroke-width="1.4" fill="none"/></svg>
    <span>hello@brightlanefixers.com</span>
  </div>
  <div class="estimate">
    <svg width="14" height="16" viewBox="0 0 14 16"><rect x="1" y="1" width="12" height="14" fill="none" stroke="#333" stroke-width="1.6"/><path d="M4 5h6M4 8h6M4 11h4" stroke="#333" stroke-width="1.4"/></svg>
    Request An Estimate
  </div>
  <div class="tail"></div>
</div>
<div class="abs navbar"></div>
<nav class="nav">
  <a href="#" class="current" style="left:626px">Home</a>
  <a href="#" style="left:756px">About Us</a>
  <a href="#" style="left:906px">Services</a>
  <a href="#" style="left:1052px">Projects</a>
</nav>

<!-- hero -->
<section class="abs hero" role="img" aria-label="Close-up of a worker in yellow gloves repairing a red tiled roof, with a red tint">
  <h1>A complete Home<br>Repair Solution</h1>
  <div class="dashes"><span></span><span></span><span></span></div>
</section>

<!-- welcome -->
<h2 class="abs title" style="top:724px">Welcome To <span class="accent">Bright Lane Fixers And Maintenance</span></h2>
<p class="abs welcome-text">Lorem ipsum dolor sit amet, consectetuer adipiscing elit, sed diam nonummy nibh euismod tincidunt ut laoreet dolore magna aliquam erat volutpat. Ut wisi enim ad minim veniam, quis nostrud exerci tation ullamcorper suscipit lobortis nisl ut aliquip ex ea commodo consequat. Duis autem vel eum iriure dolor in hendrerit in vulputate velit esse molestie consequat, vel illum dolore eu feugiat nulla facilisis at vero eros et accumsan et iusto odio dignissim qui blandit praesent luptatum zzril delenit augue duis dolore te feugait nulla facilisi.</p>
<a class="abs btn" style="left:600px;top:939px;width:97px;height:32px;text-decoration:none">Read More</a>

<!-- services -->
<section class="abs services">
  <h2 class="title light" style="position:absolute;top:30px">Our <span class="accent">Services</span></h2>
  <div class="arrow" style="left:26px"><svg width="10" height="12"><path d="M8 1L2 6l6 5" stroke="#222" stroke-width="2" fill="none"/></svg></div>
  <div class="arrow" style="left:1148px"><svg width="10" height="12"><path d="M2 1l6 5-6 5" stroke="#222" stroke-width="2" fill="none"/></svg></div>
  <div class="card active" style="left:82px">
    <div class="photo" role="img" aria-label="Carpenter in a hard hat measuring wood" style="background:linear-gradient(160deg,#8a5a34,#c99a6a 60%,#6b4a30)"></div>
    <div class="label">Carpentry</div>
  </div>
  <div class="card" style="left:344px">
    <div class="photo" role="img" aria-label="Plumber working under a sink" style="background:linear-gradient(160deg,#5b7fa8,#b5c6d8 55%,#3e5670)"></div>
    <div class="label">Plumbing</div>
  </div>
  <div class="card" style="left:606px">
    <div class="photo" role="img" aria-label="Worker fitting a wooden door frame" style="background:linear-gradient(160deg,#7a4a24,#c08a52 55%,#5a3418)"></div>
    <div class="label">Doors &amp; Windows</div>
  </div>
  <div class="card" style="left:868px">
    <div class="photo" role="img" aria-label="Electrician installing a ceiling light" style="background:linear-gradient(160deg,#c9ccd0,#eef0f2 55%,#8e949a)"></div>
    <div class="label">Electrical</div>
  </div>
</section>

<!-- projects -->
<h2 class="abs title" style="top:1516px">Our <span class="accent">Projects</span></h2>
<section class="abs projects">
  <div class="tile" role="img" aria-label="Plumber fixing chrome pipes" style="background:linear-gradient(150deg,#e8e8e8,#b0b4b8)"></div>
  <div class="tile" role="img" aria-label="Carpentry project" style="background:linear-gradient(150deg,#8a6a50,#c7a080)">
    <div class="overlay">
      <h3>Carpentry</h3>
      <p>Lorem ipsum dolouar sit ametconse consectetuer lobortis nisl</p>
      <div class="icons">
        <span><svg width="14" height="14" viewBox="0 0 14 14"><path d="M5 9l4-4M3 7l-1 1a2.5 2.5 0 0 0 4 4l1-1M11 7l1-1a2.5 2.5 0 0 0-4-4L7 3" stroke="#fff" stroke-width="1.5" fill="none"/></svg></span>
        <span><svg width="14" height="14" viewBox="0 0 14 14"><circle cx="6" cy="6" r="4" stroke="#fff" stroke-width="1.6" fill="none"/><path d="M9 9l4 4" stroke="#fff" stroke-width="1.8"/></svg></span>
      </div>
    </div>
  </div>
  <div class="tile" role="img" aria-label="Worker installing a window" style="background:linear-gradient(150deg,#6f6f6a,#b8b4a8 55%,#4a4844)"></div>
  <div class="tile" role="img" aria-label="Electrician at a wall panel" style="background:linear-gradient(150deg,#c8c2b4,#8c8272 60%,#5c5448)"></div>
  <div class="tile" role="img" aria-label="Roofer laying red roof tiles" style="background:linear-gradient(150deg,#9cc0dc,#c4584a 55%,#8a2e26)"></div>
</section>
<a class="abs btn" style="left:600px;top:1896px;width:97px;height:32px;text-decoration:none">View All</a>

<!-- why choose us -->
<section class="abs why">
  <h2 class="title small" style="position:absolute;top:44px">Why <span class="accent">Choose Us?</span></h2>
  <div class="feature" style="top:138px">
    <div class="icon"><svg width="34" height="22" viewBox="0 0 34 22"><path d="M2 10l7-7 6 3 5-3 7 4 5 4-8 8-6-4-4 2z" fill="#fff"/></svg></div>
    <h4>Our Commitment</h4>
    <p>Lorem ipsum dolouar sit amet consec tetuer adipiscing elnit. ebulum werwerwe molesbeutie lacus. Aenea noihasellu porta.</p>
  </div>
  <div class="rule" style="top:252px"></div>
  <div class="feature" style="top:276px">
    <div class="icon"><svg width="32" height="32" viewBox="0 0 32 32"><circle cx="12" cy="18" r="7" fill="none" stroke="#fff" stroke-width="4" stroke-dasharray="3 2.5"/><circle cx="12" cy="18" r="2.5" fill="#fff"/><circle cx="24" cy="8" r="5" fill="none" stroke="#fff" stroke-width="3" stroke-dasharray="2.5 2"/></svg></div>
    <h4>Personalized Attention</h4>
    <p>Lorem ipsum dolouar sit amet consec tetuer adipiscing elnit. ebulum werwerwe molesbeutie lacus. Aenea nounendrerit maurihasellu porta.</p>
  </div>
  <div class="rule" style="top:386px"></div>
  <div class="feature" style="top:409px">
    <div class="icon"><svg width="36" height="24" viewBox="0 0 36 24"><circle cx="18" cy="7" r="5" fill="#fff"/><path d="M9 24a9 9 0 0 1 18 0z" fill="#fff"/><circle cx="7" cy="9" r="3.5" fill="#fff"/><circle cx="29" cy="9" r="3.5" fill="#fff"/><path d="M0 22a7 7 0 0 1 9-6M36 22a7 7 0 0 0-9-6" fill="#fff"/></svg></div>
    <h4>Expert Team</h4>
    <p>Lorem ipsum dolouar sit amet consec tetuer adipiscing elnit. ebulum werwerwe molesbeutie lacus. Aenea nounendrerit maurihasellu porta.</p>
  </div>
</section>
<div class="abs workers" role="img" aria-label="Team of four workers in hard hats and tool belts beside a yellow ladder"></div>

<!-- testimonials -->
<h2 class="abs title small" style="top:2588px">Client <span class="accent">Testimonials</span></h2>
<div class="abs qmark" style="left:144px">&ldquo;</div>
<div class="abs qmark" style="left:1004px">&rdquo;</div>
<p class="abs quote">Lorem ipsum dolor sit amet, consectetuer adipiscing elit, sed diam nonummy nibh euismod tincidunt ut laoreet dolore magna aliquam erat volutpat. Ut wisi enim ad minim veniam, quis nostrud exerci tation ullamcorper suscipit lobortis nisl ut aliquip ex ea commodo consequat. Duis autem vel eum iriure dolor in hendrerit in vulputate velit esse</p>
<div class="abs" style="left:0;top:2778px;width:1160px;text-align:center;color:var(--red);font-size:20px;font-weight:700">Marcus</div>
<svg class="abs" style="left:568px;top:2813px" width="24" height="14"><polygon points="0,14 12,0 24,14" fill="#e0191c"/></svg>
<div class="avatar" role="img" aria-label="Client portrait" style="left:404px;top:2834px;width:104px;height:104px"></div>
<div class="avatar" role="img" aria-label="Client portrait, selected" style="left:524px;top:2826px;width:114px;height:114px;border:4px solid var(--red);background:radial-gradient(circle at 50% 40%,#c9ad95,#2c3440)"></div>
<div class="avatar" role="img" aria-label="Client portrait" style="left:654px;top:2834px;width:104px;height:104px;background:radial-gradient(circle at 50% 40%,#e2c6ae,#5a3a2a)"></div>
<div class="abs dots"><span></span><span class="on"></span><span></span></div>

<!-- footer -->
<footer class="abs footer" role="img" aria-label="Dark background of work tools"></footer>
<nav class="fnav">
  <a href="#" style="left:234px">Home</a>
  <span class="sep" style="left:354px"></span>
  <a href="#" style="left:442px">About Us</a>
  <span class="sep" style="left:586px"></span>
  <a href="#" style="left:672px">Services</a>
  <span class="sep" style="left:808px"></span>
  <a href="#" style="left:900px">Projects</a>
</nav>
<div class="abs fline"></div>

<div class="contact" style="top:3154px">
  <div class="ring"><svg width="16" height="20" viewBox="0 0 16 20"><path d="M8 0a7 7 0 0 1 7 7c0 5-7 13-7 13S1 12 1 7a7 7 0 0 1 7-7z" fill="#e0191c"/><circle cx="8" cy="7" r="2.5" fill="#1c1b1a"/></svg></div>
  <h5>Address Details</h5>
  <p>123 Lorem Ipsument volutpat<br>Aliquam Erat 12345</p>
</div>
<div class="contact" style="top:3250px">
  <div class="ring"><svg width="18" height="13" viewBox="0 0 18 13"><rect width="18" height="13" rx="2" fill="#e0191c"/><path d="M1 1l8 6 8-6" stroke="#1c1b1a" stroke-width="1.5" fill="none"/></svg></div>
  <h5>Email</h5>
  <p>hello@brightlanefixers.com</p>
</div>
<div class="contact" style="top:3336px">
  <div class="ring"><svg width="18" height="18" viewBox="0 0 24 24"><path d="M6.6 10.8a15 15 0 0 0 6.6 6.6l2.2-2.2c.3-.3.7-.4 1-.2 1.1.4 2.3.6 3.6.6.6 0 1 .4 1 1V20c0 .6-.4 1-1 1C10.6 21 3 13.4 3 4c0-.6.4-1 1-1h3.5c.6 0 1 .4 1 1 0 1.3.2 2.5.6 3.6.1.3 0 .7-.2 1z" fill="#e0191c"/></svg></div>
  <h5>Call Us</h5>
  <p>555-214-0937</p>
</div>

<div class="abs form-title">Request An Estimate</div>
<div class="field" style="top:3205px">Name*</div>
<div class="field" style="top:3254px">Email*</div>
<div class="field" style="top:3305px">Phone*</div>
<div class="field" style="top:3354px;display:flex;justify-content:space-between">Services<svg width="10" height="8" style="margin-top:4px"><path d="M1 1l4 4 4-4" stroke="#ccc" stroke-width="1.5" fill="none"/></svg></div>
<div class="abs message">Mesage*</div>
<div class="abs btn submit">Submit</div>

<div class="abs bottom">
  <span style="position:absolute;left:82px;top:13px">Copyright © 2016 Bright Lane Fixers And Maintenance LLC. All Rights Reserved.</span>
  <span style="position:absolute;left:984px;top:13px">Follow Us:</span>
  <span class="social" style="left:1060px"></span>
  <span class="social" style="left:1090px;background:#1da1f2"></span>
</div>

</body>
</html>
```